We're Hiring Poster or Flyer design

We’re Hiring Details:

Positions include:
Office Manager
Office Assistant
Data Entry Techs
Outreach Manager
Asst. Outreach Manager
Events Coordinator
Drivers (must have personal car, insurance & Driver’s License)
Outreach Specialist—Walkers
Outreach Specialist—Phone/Telemarketing (evenings only)

Excellent Pay ! Fun Atmosphere ! Bonus Pay with Promotional & Career Advancement Opportunities

***************
need 3 formats of SAME flyer:
1) 8.5 x 11
2) 8.5 x 14
3) 11 x17

creative and eye catching a must; this flyer will be used on college bulletin boards and used to attract a younger demographic . . hip and chic look with "Americana style or political motif" preferred.

Target Market(s)

younger demographic . . flyer will be used during college recruiting fairs and in younger settings---age BRACKET is 21 - 35 Years old

Industry/Entity Type

Employment Agency

Font styles to use
Sans Serif

Colors

Designer to choose colors to be used in the design.

Requirements
Must have
• clean and attractive; hip; chic; simple and with good stock pics and layout
Nice to have
• american flag and patriotism
Should not have
• too much details on the job -- I only included the job announcement so you can get an idea of WHAT and WHO I am looking for . . don't list all the BORING details on the flyer/poster

```html
<!DOCTYPE html>
<html lang="en">
<head>
<meta charset="utf-8">
<title>We're Hiring – Marcus Delgado for Mayor</title>
<link rel="stylesheet" href="https://fonts.googleapis.com/css2?family=Roboto+Condensed:wght@700&family=Source+Sans+3:ital,wght@0,400;0,600;0,700;1,400&display=swap">
<style>
  :root {
    --navy: #0b2d6b;
    --orange: #f47b20;
    --red: #c1272d;
    --white: #ffffff;
    --ink: #1a1a1a;
    --panel-gray: #cfd1d4;
  }
  * { margin: 0; padding: 0; box-sizing: border-box; }
  html, body { width: 974px; height: 1200px; overflow: hidden; background: var(--white); }
  .flyer {
    position: relative;
    width: 974px;
    height: 1200px;
    overflow: hidden;
    background: var(--white);
    font-family: "Source Sans 3", "Myriad Pro", sans-serif;
    color: var(--ink);
  }
  .backdrop { position: absolute; inset: 0; }

  .candidate-name {
    position: absolute;
    left: 55px;
    top: 66px;
    width: 310px;
    text-align: center;
    font-weight: 700;
    font-size: 56px;
    line-height: 1.02;
    color: var(--navy);
  }

  .hiring-sign {
    position: absolute;
    left: 580px;
    top: 60px;
  }
  .hiring-sign__shadow {
    position: absolute;
    left: -14px;
    top: -16px;
    width: 320px;
    height: 200px;
    background: var(--panel-gray);
    border-radius: 6px;
    transform: rotate(-2deg);
  }
  .hiring-sign__board {
    position: relative;
    width: 312px;
    height: 194px;
    background: var(--red);
    border: 4px solid var(--white);
    box-shadow: 0 2px 6px rgba(0,0,0,.25);
    display: flex;
    flex-direction: column;
    justify-content: center;
    align-items: center;
    font-family: "Roboto Condensed", "Arial Narrow", sans-serif;
    font-weight: 700;
    color: var(--white);
    font-size: 80px;
    line-height: 0.96;
    letter-spacing: 2px;
  }

  .positions-tab {
    position: absolute;
    left: 0;
    top: 326px;
    width: 497px;
    height: 60px;
    background: var(--orange);
    border-radius: 0 30px 30px 0;
    box-shadow: 2px 3px 4px rgba(0,0,0,.2);
    padding-left: 42px;
    display: flex;
    align-items: center;
    color: var(--white);
    font-weight: 700;
    font-size: 34px;
  }

  .positions-list {
    position: absolute;
    left: 36px;
    top: 405px;
    list-style: none;
    font-size: 23px;
    line-height: 36.6px;
  }
  .positions-list li {
    position: relative;
    padding-left: 33px;
  }
  .positions-list li::before {
    content: "";
    position: absolute;
    left: 0;
    top: 10px;
    width: 16px;
    height: 16px;
    border-radius: 50%;
    background: var(--navy);
  }
  .positions-list li::after {
    content: "";
    position: absolute;
    left: 4px;
    top: 15px;
    width: 5px;
    height: 5px;
    border-top: 2px solid var(--white);
    border-right: 2px solid var(--white);
    transform: rotate(45deg);
  }

  .campaign-url {
    position: absolute;
    left: 36px;
    top: 812px;
    color: var(--orange);
    font-weight: 700;
    font-size: 25px;
  }

  .contact-note {
    position: absolute;
    left: 36px;
    top: 958px;
    color: var(--white);
    font-style: italic;
    font-size: 20.5px;
    line-height: 30.5px;
  }

  .perks-banner {
    position: absolute;
    left: 81px;
    top: 1100px;
    width: 808px;
    height: 74px;
    background: var(--white);
    border: 1px solid #d8d8d8;
    border-radius: 9px;
    box-shadow: 0 2px 5px rgba(0,0,0,.25);
    text-align: center;
    color: var(--orange);
    font-size: 24px;
    line-height: 29px;
    padding-top: 8px;
  }
  .perks-banner__headline { font-weight: 700; }
  .perks-banner__detail { font-weight: 600; }
</style>
</head>
<body>
<main class="flyer">
  <svg class="backdrop" width="974" height="1200" viewBox="0 0 974 1200">
    <defs>
      <linearGradient id="flagTone" x1="0" y1="0" x2="1" y2="0.2">
        <stop offset="0" stop-color="#1c2f8c"/>
        <stop offset="0.55" stop-color="#2b3f9e"/>
        <stop offset="0.72" stop-color="#c4c7d6"/>
        <stop offset="0.85" stop-color="#d7262e"/>
        <stop offset="1" stop-color="#a9151c"/>
      </linearGradient>
      <linearGradient id="navyWave" x1="0" y1="0" x2="1" y2="1">
        <stop offset="0" stop-color="#0e3a82"/>
        <stop offset="1" stop-color="#06214f"/>
      </linearGradient>
      <linearGradient id="photoTone" x1="0" y1="0" x2="1" y2="0">
        <stop offset="0" stop-color="#3a3a3f"/>
        <stop offset="0.5" stop-color="#6b6d72"/>
        <stop offset="1" stop-color="#b1b4b8"/>
      </linearGradient>
    </defs>
    <path d="M0 905 C150 880 300 895 400 970 C470 1025 505 1110 520 1200 H0 Z" fill="url(#navyWave)"/>
    <g role="img" aria-label="Waving American flag with stars and stripes">
      <path d="M674 0 H974 V1100 H450 C470 950 500 800 560 660 C620 520 660 420 650 300 C645 200 660 90 674 0 Z" fill="url(#flagTone)"/>
    </g>
    <g role="img" aria-label="Photo of a smiling businesswoman and businessman in suits, arms crossed">
      <path d="M430 1200 V700 Q430 470 650 470 H974 V1200 Z" fill="url(#photoTone)" opacity="0.92"/>
    </g>
  </svg>

  <div class="candidate-name">Marcus<br>Delgado<br>for Mayor</div>

  <div class="hiring-sign">
    <div class="hiring-sign__shadow"></div>
    <div class="hiring-sign__board"><span>WE'RE</span><span>HIRING</span></div>
  </div>

  <h2 class="positions-tab">POSITIONS INCLUDE:</h2>

  <ul class="positions-list">
    <li>Office Manager</li>
    <li>Office Assistant</li>
    <li>Data Entry Techs</li>
    <li>Outreach Manager</li>
    <li>Asst. Outreach Manager</li>
    <li>Events Coordinator</li>
    <li>Drivers (must have personal car,<br>insurance &amp; Driver’s License)</li>
    <li>Outreach Specialist - Walkers</li>
    <li>Outreach Specialist - Phone/<br>Telemarketing (evenings only)</li>
  </ul>

  <p class="campaign-url">www.delgadoformayor.com</p>

  <p class="contact-note">Please email this job order to<br>hiring@civicworkscenter.org<br>Questions call Renata Holt<br>555-014-2290</p>

  <div class="perks-banner">
    <div class="perks-banner__headline">EXCELLENT PAY ! FUN ATMOSPHERE !</div>
    <div class="perks-banner__detail">Bonus Pay with Promotional &amp; Career Advancement Opportunities</div>
  </div>
</main>
</body>
</html>
```